event catering company brochure & menus

i have a collaboration of different menus that i would like redesigning each one for expanding my company to the uae

Along with this i would like them to be formatted into a brochure to use & photos attached to what is suitable

Target Market(s)

corperate customers

Industry/Entity Type

catering

```html
<!DOCTYPE html>
<html lang="en">
<head>
<meta charset="utf-8">
<title>Verdelia – Catering Brochure</title>
<link rel="stylesheet" href="https://fonts.googleapis.com/css2?family=Poppins:wght@300;400;500;600;700&display=swap">
<style>
  :root{
    --backdrop:#dfe0e2;
    --paper:#ffffff;
    --charcoal:#333235;
    --ink:#1f1f21;
    --body-ink:#3a3a3c;
    --on-dark:#f4f4f4;
    --soft-grey:#e6e6e8;
  }
  *{margin:0;padding:0;box-sizing:border-box}
  html,body{width:1110px;height:1200px;overflow:hidden}
  body{background:var(--backdrop);font-family:"Poppins",sans-serif;color:var(--ink);position:relative}

  .page{position:absolute;width:367px;height:520px;background:var(--paper);box-shadow:0 2px 6px rgba(0,0,0,.18);overflow:hidden}
  .page--kids{left:70px;top:50px}
  .page--cover{left:476px;top:50px}
  .page--about{left:268px;top:618px;height:519px}
  .page--gallery{left:673px;top:618px;height:519px}

  .photo{position:absolute;display:block}
  .abs{position:absolute}

  /* children's menu */
  .kids-hero{left:0;top:6px;width:367px;height:164px;background:linear-gradient(135deg,#4a2a18 0%,#8a4f26 35%,#c98f48 60%,#e3dcd2 75%,#3a2416 100%)}
  .kids-wordmark{left:0;top:16px;width:367px;text-align:center;color:#fff;font-weight:300;font-size:27px;letter-spacing:11px;padding-left:11px}
  .kids-title{left:0;top:55px;width:367px;text-align:center;color:#fff;font-weight:700;font-size:13px}
  .kids-dark{left:188px;top:170px;width:164px;height:350px;background:var(--charcoal)}
  .kids-side-photo{left:0;top:398px;width:188px;height:104px;background:linear-gradient(160deg,#bccbd6 0%,#e8e1d6 40%,#c7873e 70%,#8c5424 100%)}
  .dish{position:absolute;font-size:6.8px;line-height:9px;font-weight:300}
  .dish h3{font-size:7.6px;line-height:9.4px;font-weight:700;text-transform:uppercase}
  .dish .sep{margin-top:6px}
  .dish--left{left:22px;width:148px;color:var(--ink)}
  .dish--right{left:198px;width:146px;color:var(--on-dark)}
  .dish--right h3{color:#fff}
  .dish--small h3{font-size:5.6px;line-height:7.2px}
  .dish--small p{font-size:5.6px;line-height:7px}

  /* cover */
  .cover-band{left:0;top:0;width:367px;height:22px;background:var(--charcoal)}
  .cover-wordmark{left:40px;top:58px;font-size:30px;font-weight:300;letter-spacing:13.5px;color:var(--ink)}
  .cover-photo-a{left:0;top:112px;width:191px;height:255px;background:linear-gradient(140deg,#7a4b22 0%,#b0793d 35%,#6c7a2e 60%,#9c6430 100%)}
  .cover-photo-b{left:195px;top:112px;width:160px;height:126px;background:linear-gradient(150deg,#5b3f2e 0%,#d0643a 45%,#6a4a36 80%,#c9c6c2 100%)}
  .cover-photo-c{left:195px;top:241px;width:160px;height:125px;background:linear-gradient(150deg,#e8e8e6 0%,#c77c3d 40%,#8e3b35 60%,#e8e8e6 100%)}
  .cover-tagline{left:33px;top:396px;font-size:18px;line-height:21.5px;font-weight:300;color:var(--ink);text-transform:uppercase}

  /* shared text */
  .copy{position:absolute;font-size:7px;line-height:8.2px;font-weight:300;color:var(--body-ink)}
  .copy p+p{margin-top:8px}
  .footer-mark{position:absolute;left:292px;top:496px;font-size:7px;font-weight:300;letter-spacing:3px;color:var(--ink)}

  /* about */
  .about-wedge{left:0;top:0;width:367px;height:52px}
  .about-band{left:0;top:22px;width:367px;height:30px;background:var(--charcoal);color:#fff;font-weight:700;font-size:14.5px;line-height:30px;padding-left:26px}
  .about-photo{left:0;top:52px;width:367px;height:220px;background:linear-gradient(150deg,#dfe3e1 0%,#cfd7cf 30%,#d4703f 50%,#8fae3c 62%,#e9eceb 85%);clip-path:polygon(0 0,100% 6px,100% 271px,0 147px)}
  .about-col-a{left:26px;top:247px;width:152px}
  .about-col-b{left:198px;top:283px;width:152px}
  .about-photo-small{left:26px;top:424px;width:152px;height:95px;background:linear-gradient(170deg,#2a3550 0%,#c9ced6 45%,#f2f2f2 70%,#b85a2f 100%)}

  /* gallery */
  .gallery-title{left:26px;top:29px;font-weight:700;font-size:14.5px;color:var(--ink)}
  .gallery-photo-a{left:0;top:56px;width:260px;height:130px;background:linear-gradient(120deg,#f0c79a 0%,#8e8a5e 40%,#d7a475 55%,#2c2a2b 80%)}
  .gallery-photo-b{left:274px;top:56px;width:93px;height:130px;background:linear-gradient(160deg,#f1f1f0 0%,#8e3f3a 40%,#d7953c 65%,#eceeea 100%)}
  .gallery-dark{left:13px;top:185px;width:175px;height:334px;background:var(--charcoal)}
  .gallery-col-a{left:26px;top:208px;width:152px;color:var(--on-dark)}
  .gallery-col-b{left:197px;top:208px;width:153px}
  .gallery-photo-c{left:197px;top:340px;width:152px;height:137px;background:linear-gradient(150deg,#f3f3f3 0%,#d64b33 35%,#5a8a2c 55%,#f0e9d8 75%,#f3f3f3 100%)}
</style>
</head>
<body>

<!-- Children's menu page -->
<section class="page page--kids">
  <div class="photo kids-hero" role="img" aria-label="Photo of a brioche burger with crispy onions and fries"></div>
  <div class="abs kids-wordmark">VERDELIA</div>
  <h1 class="abs kids-title">SAMPLE CHILDREN’S MENU</h1>
  <div class="abs kids-dark"></div>
  <div class="photo kids-side-photo" role="img" aria-label="Photo of a burger with potato wedges on a plate"></div>

  <div class="dish dish--left" style="top:195px">
    <h3>Homemade Margherita Pizza</h3>
    <p>(Other flavours available)<br>Fresh rocket</p>
    <p class="sep">--</p>
  </div>
  <div class="dish dish--left" style="top:249px">
    <h3>Corn Fed Chicken Goujons</h3>
    <p>Hand cut chips &amp; roasted vegetables</p>
    <p class="sep">--</p>
  </div>
  <div class="dish dish--left" style="top:294px">
    <h3>Homemade Cod Fish Fingers or Fish Cakes</h3>
    <p>Fresh peas &amp; thrice cooked chips &amp;<br>herb mayonnaise</p>
    <p class="sep">--</p>
  </div>
  <div class="dish dish--left" style="top:358px">
    <h3>Sirloin of Beef Burger with Cheddar Cheese in a Brioche Bap</h3>
    <p>Chips &amp; mixed salad<br>--</p>
  </div>

  <div class="dish dish--right" style="top:195px">
    <h3>Griddled Chicken Breast</h3>
    <p>Roasted potatoes, barbecue sauce &amp;<br>mixed vegetables</p>
    <p class="sep">--</p>
  </div>
  <div class="dish dish--right" style="top:249px">
    <h3>Fresh Tagliatelle</h3>
    <p>Oven dried tomato sauce &amp; basil &amp;<br>rocket<br>Served with garlic bruschetta</p>
  </div>
  <div class="dish dish--right" style="top:296px"><h3>Dessert</h3></div>
  <div class="dish dish--right dish--small" style="top:311px">
    <h3>Chocolate Brownie Sundae</h3>
    <p>Caramel sauce, vanilla ice cream &amp; chocolate<br>crumb</p>
    <p class="sep">--</p>
  </div>
  <div class="dish dish--right dish--small" style="top:356px">
    <h3>Fresh Strawberries with Vanilla Ice<br>Cream &amp; Strawberry Coulis</h3>
    <p class="sep">--</p>
  </div>
  <div class="dish dish--right dish--small" style="top:393px">
    <h3>Assiette of Fresh Fruit Plate</h3>
  </div>
</section>

<!-- Cover page -->
<section class="page page--cover">
  <div class="abs cover-band"></div>
  <div class="abs cover-wordmark">VERDELIA</div>
  <div class="photo cover-photo-a" role="img" aria-label="Photo of canapé tartlets with green garnish on a wooden board"></div>
  <div class="photo cover-photo-b" role="img" aria-label="Photo of smoked salmon canapés on a slate board"></div>
  <div class="photo cover-photo-c" role="img" aria-label="Photo of plated duck breast with orange and carrots"></div>
  <h2 class="abs cover-tagline" style="font-weight:300">Dubai’s most exclusive<br>private catering company<br>servicing across the<br>UAE &amp; Middle East</h2>
</section>

<!-- About page -->
<section class="page page--about">
  <svg class="abs about-wedge" viewBox="0 0 367 52" width="367" height="52" aria-hidden="true">
    <polygon points="0,0 367,0 367,22 0,5" fill="#ffffff"/>
    <polygon points="0,5 367,22 0,22" fill="#e6e6e8"/>
  </svg>
  <h2 class="abs about-band">SERVICING ACROSS THE UAE &amp; MIDDLE EAST</h2>
  <div class="photo about-photo" role="img" aria-label="Photo of a plated crab starter with grapefruit, radish and herb oil"></div>

  <div class="copy about-col-a">
    <p>A great dining experience should leave more than a great taste in your mouth. That’s why Verdelia Events combine the best flavours with first-class customer service to deliver outstanding private dining experiences.</p>
    <p>Whether you’re looking for a caterer in Dubai, bespoke catering in Abu Dhabi or even a private chef for an intimate dinner party Ras al-Khaimah, Verdelia have been catering exclusive private events since 2013.</p>
    <p>Verdelia Events is one of the United Kingdoms finest catering companies, with a reputation now across the United Arab Emirates so we have expanded our operation to provide our services throughout the Middle East.</p>
  </div>
  <div class="copy about-col-b">
    <p>Whether you’re looking to impress friends or family with an intimate dinner party in your home or make a special date one to remember thanks to exceptional catering, if you are looking at planning a party or event which needs calls for an experienced &amp; discreet catering company, Verdelia have the skill, attention to detail and experience to bring your dining ideas to life.</p>
    <p>Tailored to you, each menu is designed to suit your occasion, personal tastes and desired ambience. Our staff work tirelessly to ensure that all details are in and offer a discreet, unobtrusive yet responsive service.</p>
  </div>
  <div class="photo about-photo-small" role="img" aria-label="Photo of a server holding a plate of canapés"></div>
  <div class="footer-mark">VERDELIA</div>
</section>

<!-- Gallery page -->
<section class="page page--gallery">
  <h2 class="abs gallery-title">SERVICING ACROSS THE UAE &amp; MIDDLE EAST</h2>
  <div class="photo gallery-photo-a" role="img" aria-label="Photo of decorated macarons on a platter of rosemary held by a chef"></div>
  <div class="photo gallery-photo-b" role="img" aria-label="Photo of sliced roast beef with roasted vegetables"></div>
  <div class="abs gallery-dark"></div>
  <div class="copy gallery-col-a">
    <p>A great dining experience should leave more than a great taste in your mouth. That’s why Verdelia Events combine the best flavours with first-class customer service to deliver outstanding private dining experiences. Whether you’re looking for a caterer in Dubai, bespoke catering in Abu Dhabi or even a private chef for an intimate dinner party Ras al-Khaimah, Verdelia have been catering exclusive private events since 2013. Verdelia Events is one of the United Kingdoms finest catering companies, with a reputation now across the United Arab Emirates so we have expanded our operation to provide our services throughout the Middle East.</p>
  </div>
  <div class="copy gallery-col-b">
    <p>Whether you’re looking to impress friends or family with an intimate dinner party in your home or make a special date one to remember thanks to exceptional catering, if you are looking at planning a party or event which needs calls for an experienced &amp; discreet catering company, Verdelia have the skill, attention to detail and experience to bring your dining ideas to life.</p>
    <p>Tailored to you, each menu is designed to suit your occasion, personal tastes and desired ambience. Our staff work tirelessly to ensure that all details are in and offer a discreet, unobtrusive yet responsive service.</p>
  </div>
  <div class="photo gallery-photo-c" role="img" aria-label="Photo of plated white fish with tomatoes, spinach and herb salsa"></div>
  <div class="footer-mark">VERDELIA</div>
</section>

</body>
</html>
```